BrightHarbor Flowchart Marketing Flyer

We are an MSP IT company. We have created a flowchart that we would like jazzed up to use in marketing new customers. The flowchart is a visual for prospective clients to see, in a simple way, what our process is. The flowchart should be 8.5"x11". We do not want the template of the flowchart altered (no boxes moved around) but would like something visually appealing and clean looking. Our office colors are lime green, royal blue, with accent colors of orange and purple. We would like the colors incorporated into the design. The design should be modern. This flyer is not going to be mass mailed. It will be handed to a prospective client in a face to face meeting.
Updates

I have uploaded our company logo to my brief in a couple of formats. One of the designers requested this. Great idea! I apologize for not providing it to begin with - it's my first time using this Website and the first time I have been assigned a project.

I was not able to view over the weekend as I did not have access to my work computer. Also need to review with the rest of management team on Thursday 6/28

Target Market(s)

Potential clients for an MSP IT company

Industry/Entity Type

It Company

Requirements
Must have
• The template itself we don't want changed. In other words we don't want the boxes moved around.
Nice to have
• Text, lines, shading and color of boxes can be changed. Not all colors mentioned in the brief need to be used. Would like it easy on the eye.

```html
<!DOCTYPE html>
<html lang="en">
<head>
<meta charset="utf-8">
<title>BrightHarbor Process</title>
<link href="https://fonts.googleapis.com/css2?family=Arimo:wght@400;700&display=swap" rel="stylesheet">
<style>
  :root {
    --navy-deep: #0d0f4c;
    --navy-mid: #14307e;
    --royal: #1b5aa8;
    --title-navy: #29296d;
    --orange: #f7941d;
    --box-fill: #a1a9d0;
    --panel-fill: #9a9ec6;
    --white: #ffffff;
  }
  html, body {
    margin: 0;
    padding: 0;
    width: 1200px;
    height: 927px;
    overflow: hidden;
  }
  body {
    font-family: "Arimo", Arial, sans-serif;
    position: relative;
    background:
      linear-gradient(155deg, transparent 30%, rgba(40, 110, 200, 0.35) 42%, transparent 55%),
      linear-gradient(20deg, transparent 45%, rgba(30, 90, 180, 0.3) 58%, transparent 70%),
      radial-gradient(ellipse 700px 500px at 420px 380px, var(--royal) 0%, var(--navy-mid) 45%, var(--navy-deep) 100%);
  }
  .header-band {
    position: absolute;
    left: 0; top: 27px;
    width: 1200px; height: 109px;
    background: var(--orange);
  }
  .page-title {
    position: absolute;
    left: 55px; top: 50px;
    margin: 0;
    font-size: 55px;
    font-weight: 700;
    color: var(--title-navy);
    letter-spacing: 0.2px;
  }
  .brand {
    position: absolute;
    left: 960px; top: 60px;
    display: flex;
    align-items: center;
    gap: 10px;
  }
  .brand-dot {
    width: 34px; height: 34px;
    border-radius: 50%;
    background: var(--title-navy);
  }
  .brand-name {
    font-size: 32px;
    font-weight: 700;
    color: var(--title-navy);
  }
  .step {
    position: absolute;
    top: 364px;
    width: 158px; height: 80px;
    background: var(--box-fill);
    border: 2px solid var(--orange);
    border-radius: 11px;
    display: flex;
    align-items: center;
    justify-content: center;
    text-align: center;
    font-size: 21px;
    font-weight: 700;
    line-height: 25px;
    color: var(--title-navy);
  }
  .step-assess { left: 56px; }
  .step-onboard { left: 294px; }
  .step-eval { left: 528px; }
  .strategy-panel {
    position: absolute;
    left: 768px; top: 254px;
    width: 376px; height: 304px;
    border-radius: 12px;
    background: var(--panel-fill);
    overflow: hidden;
  }
  .panel-head {
    height: 38px;
    background: var(--orange);
    color: var(--title-navy);
    font-size: 20px;
    font-weight: 700;
    line-height: 38px;
    padding-left: 18px;
  }
  .cycle-box {
    position: absolute;
    width: 96px; height: 54px;
    background: var(--orange);
    border: 2px solid var(--white);
    display: flex;
    align-items: center;
    justify-content: center;
    text-align: center;
    font-size: 15.5px;
    line-height: 21px;
    color: var(--title-navy);
  }
  .cycle-strategy { left: 134px; top: 58px; }
  .cycle-risk { left: 30px; top: 128px; }
  .cycle-standards { left: 244px; top: 128px; }
  .cycle-budget { left: 134px; top: 203px; }
  .connectors {
    position: absolute;
    left: 0; top: 0;
  }
  .detail-list {
    position: absolute;
    margin: 0;
    padding: 0;
    list-style: none;
    color: var(--white);
    font-size: 14.5px;
    line-height: 21.2px;
  }
  .detail-list li::before {
    content: "\2022";
    color: var(--orange);
    margin-right: 6px;
  }
  .list-assess { left: 69px; top: 502px; }
  .list-onboard { left: 303px; top: 502px; }
  .list-eval { left: 528px; top: 502px; }
  .list-strategy { left: 779px; top: 612px; }
  sup { font-size: 8px; }
</style>
</head>
<body>
  <div class="header-band"></div>
  <h1 class="page-title">BrightHarbor Process</h1>
  <div class="brand"><span class="brand-dot"></span><span class="brand-name">Tidewell</span></div>

  <svg class="connectors" width="1200" height="927" viewBox="0 0 1200 927" aria-hidden="true">
    <g fill="none" stroke="#f7941d" stroke-width="2">
      <!-- flow arrows -->
      <line x1="218" y1="406" x2="288" y2="406"/>
      <line x1="456" y1="406" x2="522" y2="406"/>
      <line x1="692" y1="406" x2="760" y2="406"/>
      <!-- callout lines -->
      <path d="M138 448 V472 Q138 482 128 482 H64 Q54 482 54 492 V560"/>
      <path d="M375 448 V472 Q375 482 365 482 H301 Q291 482 291 492 V577"/>
      <path d="M611 448 V472 Q611 482 601 482 H527 Q517 482 517 492 V577"/>
      <path d="M956 558 V578 Q956 588 946 588 H778 Q768 588 768 598 V724"/>
    </g>
    <g fill="#f7941d">
      <polygon points="294,406 286,402 286,410"/>
      <polygon points="528,406 520,402 520,410"/>
      <polygon points="766,406 758,402 758,410"/>
      <circle cx="54" cy="560" r="3"/>
      <circle cx="291" cy="577" r="3"/>
      <circle cx="517" cy="577" r="3"/>
      <circle cx="768" cy="724" r="3"/>
    </g>
    <!-- cycle arcs -->
    <g fill="none" stroke="#f7941d" stroke-width="3">
      <path d="M838 370 Q840 332 882 328"/>
      <path d="M1018 328 Q1058 332 1060 370"/>
      <path d="M1058 448 Q1056 486 1016 490"/>
      <path d="M882 490 Q840 486 838 448"/>
    </g>
  </svg>

  <div class="step step-assess">Assess<br>Alignment</div>
  <div class="step step-onboard">On Boarding</div>
  <div class="step step-eval">30 Day<br>Evaluation</div>

  <section class="strategy-panel">
    <div class="panel-head">Ongoing Strategic Plan &amp; Execution</div>
    <div class="cycle-box cycle-strategy">Strategy</div>
    <div class="cycle-box cycle-risk">Risk<br>Assessment</div>
    <div class="cycle-box cycle-standards">Standards<br>Alignment</div>
    <div class="cycle-box cycle-budget">Budget</div>
  </section>

  <ul class="detail-list list-assess">
    <li>Review Technology Philosophy</li>
    <li>Share Proprietary Method</li>
    <li>Assess Organizational Fit</li>
  </ul>
  <ul class="detail-list list-onboard">
    <li>Establish Expectations</li>
    <li>Service Provider Transition</li>
    <li>Cybersecurity Review</li>
    <li>Backup/Protection Strategy</li>
  </ul>
  <ul class="detail-list list-eval">
    <li>Develop IT Playbook</li>
    <li>Major Risk Identification</li>
    <li>Observe &amp; Document Trends</li>
    <li>Standards Alignment Plan</li>
  </ul>
  <ul class="detail-list list-strategy">
    <li>Develop &amp; Execute Annual Strategic Plan</li>
    <li>Risk Assessment, Ranking, Mitigation</li>
    <li>Prioritize Investments</li>
    <li>Develop 5 Year Budget</li>
    <li>TideSolution<sup>TM</sup> Standard Alignment</li>
  </ul>
</body>
</html>
```